e-commerce website for selling flooring materials and related accessories

We are developing a new e-commerce site based in the US. We plan to sell all types of flooring - such as Hardwood, Laminate, Waterproof flooring and Porcelain tile, marble, Carpet, and related accessories.

OUR BACK END IS MAGENTO 2.

Target Market(s)

consumer, builder & contractors, hospitality industry, architect, designers, private sector

Industry/Entity Type

Flooring

Coding

Coded - Design and coding required

Number of Pages Required

5+ page

Font styles to use
Sans Serif

Requirements
Must have
• Logo placement, 3 Color combination, Banner placement, promotional pricing tags, check out page, blog placement, social media icons, 1800 number, product and related accessories placement. For reference purposes, please visit our competitor websites -
1.www.plankmeadowoutlet.example
2.tilebirchhome.example
3.www.grovewoodsurplus.example
4.www.shopkestrel.example
5.www.padmatcorp.example
Nice to have
• Our main customers are women and families and we want to make sure the design is attractive.
we like to have 2 or 3 bands at the top.
please provide design for the bottom page.
Should not have
• As our products are more natural colors, please do not bring extreme colors into the design

```html
<!DOCTYPE html>
<html lang="en">
<head>
<meta charset="utf-8">
<title>Plankhaven – Homepage Variants</title>
<link href="https://fonts.googleapis.com/css2?family=Open+Sans:wght@400;600;700;800&display=swap" rel="stylesheet">
<style>
:root{
  --orange:#ee7d1c;
  --orange-dark:#d66a0e;
  --navy:#1e2c4b;
  --navy-soft:#2b3b5e;
  --ink:#2a2a2a;
  --muted:#7a7a7a;
  --line:#e3e3e3;
  --canvas:#eeeeee;
  --paper:#ffffff;
  --footer:#232323;
  --footer-deep:#181818;
  --wood-light:#caa57a;
  --wood-mid:#a87a4c;
  --wood-dark:#6e4b2d;
  --stone:#c9c4bb;
}
*{box-sizing:border-box;margin:0;padding:0}
html,body{width:1200px;height:2593px;overflow:hidden}
body{background:var(--canvas);font-family:"Open Sans",Arial,sans-serif;color:var(--ink);position:relative}
.page{position:absolute;top:20px;width:540px;height:2553px;background:var(--paper);box-shadow:0 0 6px rgba(0,0,0,.12);overflow:hidden;display:flex;flex-direction:column}
.page--a{left:40px}
.page--b{left:620px}
.ph{display:block}
.ph--wood{background:linear-gradient(135deg,var(--wood-light),var(--wood-mid))}
.ph--dark{background:linear-gradient(135deg,var(--wood-mid),var(--wood-dark))}
.ph--stone{background:linear-gradient(135deg,#ddd8cf,var(--stone))}
.ph--room{background:linear-gradient(160deg,#e9e4dc 0%,#d4c8b6 55%,#a98457 100%)}
.ph--grey{background:linear-gradient(135deg,#d9d9d9,#b4b4b4)}

/* top bands */
.topbar{height:10px;background:var(--orange)}
.header{height:44px;display:flex;align-items:center;padding:0 16px;gap:14px}
.brand{display:flex;align-items:center;gap:6px;font-weight:800;font-size:17px;color:var(--orange)}
.brand__mark{width:14px;height:14px;background:var(--orange)}
.search{flex:1;height:20px;border:1px solid var(--line);display:flex;align-items:center;justify-content:space-between;padding-left:6px;font-size:7px;color:var(--muted)}
.search__btn{width:22px;height:18px;background:var(--orange)}
.contact{display:flex;gap:10px;font-size:6.5px;color:var(--muted);line-height:1.3}
.contact b{display:block;color:var(--ink);font-size:7px}
.nav{height:22px;background:var(--navy);display:flex;align-items:center;padding:0 16px;gap:2px}
.nav a{font-size:7px;color:#fff;text-decoration:none;padding:0 8px;line-height:22px}
.nav a.is-active{background:var(--orange)}

/* hero */
.hero{height:220px;position:relative;display:flex;align-items:center;justify-content:center}
.hero__title{position:relative;color:#fff;font-weight:800;font-size:22px;letter-spacing:1px;text-shadow:0 1px 3px rgba(0,0,0,.25)}
.hero__dots{position:absolute;bottom:12px;left:50%;transform:translateX(-50%);display:flex;gap:5px}
.hero__dots i{width:6px;height:6px;border-radius:50%;background:rgba(255,255,255,.6)}
.hero__dots i:first-child{background:var(--orange)}

/* promo strip */
.promo{height:56px;display:flex;border-bottom:1px solid var(--line)}
.promo__cell{flex:1;display:flex;align-items:center;justify-content:center;gap:6px;border-right:1px solid var(--line)}
.promo__cell:last-child{border-right:0}
.promo__big{font-size:22px;font-weight:800;color:var(--orange)}
.promo__small{font-size:6.5px;color:var(--muted);line-height:1.3;text-transform:uppercase}

/* features */
.features{height:110px;display:flex;align-items:center;justify-content:space-around;padding:0 30px}
.feature{text-align:center;width:90px}
.feature svg{width:26px;height:26px;margin-bottom:6px}
.feature h4{font-size:6.5px;font-weight:700}
.feature p{font-size:5.5px;color:var(--muted);margin-top:2px}

/* generic section */
.section{padding:14px 20px 0}
.section__title{text-align:center;font-size:12px;font-weight:700;margin-bottom:12px}
.grid4{display:grid;grid-template-columns:repeat(4,1fr);gap:8px}
.grid3{display:grid;grid-template-columns:repeat(3,1fr);gap:10px}
.cats{height:210px}
.cat .ph{height:110px}
.cat p{font-size:6.5px;text-align:center;font-weight:600;margin-top:6px;text-transform:uppercase}
.products{height:230px}
.card{border:1px solid var(--line)}
.card .ph{height:95px}
.card__body{padding:6px;font-size:6px;color:var(--muted);line-height:1.4}
.card__price{color:var(--orange);font-weight:700;font-size:7.5px;margin-top:3px}
.card__btn{display:block;margin:0 6px 6px;height:14px;background:var(--navy);color:#fff;font-size:6px;text-align:center;line-height:14px}

/* banner */
.banner{height:190px;margin-top:6px;position:relative;display:flex;align-items:center;justify-content:center}
.banner__text{position:relative;text-align:center;color:var(--navy)}
.banner__text h3{font-size:20px;font-weight:800;line-height:1.1}
.banner__text p{font-size:7px;margin-top:4px}
.banner__text span{display:inline-block;margin-top:8px;background:var(--orange);color:#fff;font-size:6.5px;padding:3px 10px}

.best{height:250px}
.best .card .ph{height:110px}

/* reviews */
.reviews{height:190px;background:var(--navy);color:#fff;padding:16px 30px 0}
.reviews .section__title{color:#fff}
.review{font-size:6px;line-height:1.5;color:#d5dae4}
.review b{display:block;color:var(--orange);font-size:6.5px;margin-top:6px}
.review__stars{color:var(--orange);font-size:8px;letter-spacing:1px;margin-bottom:4px}
.page--b .reviews{background:var(--paper);color:var(--ink);border-top:1px solid var(--line);border-bottom:1px solid var(--line)}
.page--b .reviews .section__title{color:var(--ink)}
.page--b .review{color:var(--muted)}

.recommended{height:200px}
.recommended .ph{height:125px}

/* history */
.history{height:280px}
.history__row{display:flex;gap:14px}
.history__row .ph{width:230px;height:190px;flex:none}
.history__text{font-size:6.5px;line-height:1.6;color:var(--muted)}
.history__text p{margin-bottom:8px}
.btn{display:inline-block;background:var(--orange);color:#fff;font-size:6.5px;padding:4px 12px;font-weight:600}

.blogs{height:210px}
.blog .ph{height:105px}
.blog h5{font-size:7px;margin-top:6px}
.blog p{font-size:6px;color:var(--muted);margin-top:3px;line-height:1.4}

/* signup */
.signup{height:100px;background:#f6f6f6;text-align:center;padding-top:22px}
.signup h3{font-size:12px;font-weight:700}
.signup form{display:flex;justify-content:center;margin-top:12px}
.signup__input{width:220px;height:22px;border:1px solid var(--line);background:#fff;font-size:7px;color:var(--muted);text-align:left;padding:6px}
.signup__btn{height:22px;background:var(--orange);color:#fff;font-size:7px;padding:0 14px;line-height:22px;font-weight:600}

/* footer */
.payments{height:30px;background:#fff;display:flex;align-items:center;justify-content:space-between;padding:0 20px}
.payments__cards{display:flex;gap:5px}
.payments__cards i{width:24px;height:14px;background:var(--stone);border-radius:2px}
.payments__note{font-size:8px;font-weight:700;color:var(--navy)}
.footer{height:170px;background:var(--footer);color:#bdbdbd;padding:16px 20px 0;display:grid;grid-template-columns:repeat(4,1fr);gap:12px}
.footer h6{font-size:7px;color:#fff;margin-bottom:8px;text-transform:uppercase}
.footer li{list-style:none;font-size:6px;line-height:1.9}
.socials{display:flex;gap:5px;margin-top:8px}
.socials i{width:12px;height:12px;border-radius:50%;background:#555}
.footbar{height:31px;background:var(--footer-deep);color:#8d8d8d;font-size:6px;display:flex;align-items:center;justify-content:space-between;padding:0 20px}
</style>
</head>
<body>

<!-- Variant A: navy review band -->
<section class="page page--a">
  <div class="topbar"></div>
  <header class="header">
    <div class="brand"><span class="brand__mark"></span>Plankhaven</div>
    <div class="search">Search products… <span class="search__btn"></span></div>
    <div class="contact"><div><b>1-800-555-0142</b>Call us today</div><div><b>hello@plankhaven.example</b>Email support</div></div>
  </header>
  <nav class="nav"><a class="is-active">Home</a><a>Hardwood</a><a>Laminate</a><a>Waterproof</a><a>Tile &amp; Stone</a><a>Carpet</a><a>Accessories</a><a>Blog</a></nav>
  <div class="hero ph ph--room" role="img" aria-label="Bright living room with light wood plank flooring">
    <span class="hero__title">UPGRADE YOUR FLOORS</span>
    <div class="hero__dots"><i></i><i></i><i></i></div>
  </div>
  <div class="promo">
    <div class="promo__cell"><span class="promo__big">3%</span><span class="promo__small">Off your<br>first order</span></div>
    <div class="promo__cell"><span class="promo__big">12</span><span class="promo__small">Months<br>financing</span></div>
    <div class="promo__cell"><span class="promo__big">$99</span><span class="promo__small">Flat rate<br>shipping</span></div>
  </div>
  <div class="features">
    <div class="feature"><svg viewBox="0 0 26 26"><rect x="3" y="8" width="20" height="14" fill="none" stroke="#ee7d1c" stroke-width="2"/><path d="M3 8l10-5 10 5" fill="none" stroke="#ee7d1c" stroke-width="2"/></svg><h4>FREE SAMPLES</h4><p>Try before you buy</p></div>
    <div class="feature"><svg viewBox="0 0 26 26"><rect x="2" y="9" width="14" height="10" fill="none" stroke="#ee7d1c" stroke-width="2"/><path d="M16 12h5l3 4v3h-8" fill="none" stroke="#ee7d1c" stroke-width="2"/><circle cx="7" cy="21" r="2" fill="#ee7d1c"/><circle cx="20" cy="21" r="2" fill="#ee7d1c"/></svg><h4>FAST DELIVERY</h4><p>Nationwide shipping</p></div>
    <div class="feature"><svg viewBox="0 0 26 26"><path d="M13 3l9 4v6c0 6-4 9-9 10-5-1-9-4-9-10V7z" fill="none" stroke="#ee7d1c" stroke-width="2"/><path d="M9 13l3 3 5-6" fill="none" stroke="#ee7d1c" stroke-width="2"/></svg><h4>PRICE MATCH</h4><p>Best price promise</p></div>
    <div class="feature"><svg viewBox="0 0 26 26"><path d="M5 5h4l3 6-2 2a12 12 0 005 5l2-2 6 3v4c-10 1-19-8-18-18z" fill="none" stroke="#ee7d1c" stroke-width="2"/></svg><h4>EXPERT HELP</h4><p>Talk to a specialist</p></div>
  </div>
  <div class="section cats">
    <h2 class="section__title">Shop Popular Categories</h2>
    <div class="grid4">
      <div class="cat"><span class="ph ph--dark" role="img" aria-label="Hardwood flooring sample"></span><p>Hardwood Flooring</p></div>
      <div class="cat"><span class="ph ph--wood" role="img" aria-label="Laminate flooring sample"></span><p>Laminate Flooring</p></div>
      <div class="cat"><span class="ph ph--stone" role="img" aria-label="Porcelain tile sample"></span><p>Porcelain Tile</p></div>
      <div class="cat"><span class="ph ph--grey" role="img" aria-label="Waterproof vinyl flooring sample"></span><p>Waterproof Flooring</p></div>
    </div>
  </div>
  <div class="section products">
    <h2 class="section__title">Featured Products</h2>
    <div class="grid4">
      <div class="card"><span class="ph ph--wood" role="img" aria-label="Oak plank product"></span><div class="card__body">Natural oak plank, 5 in wide<div class="card__price">$3.49 / sq ft</div></div><span class="card__btn">Add to Cart</span></div>
      <div class="card"><span class="ph ph--dark" role="img" aria-label="Walnut plank product"></span><div class="card__body">Walnut hand-scraped plank<div class="card__price">$4.29 / sq ft</div></div><span class="card__btn">Add to Cart</span></div>
      <div class="card"><span class="ph ph--stone" role="img" aria-label="Marble tile product"></span><div class="card__body">Honed marble tile, 12 x 24<div class="card__price">$5.99 / sq ft</div></div><span class="card__btn">Add to Cart</span></div>
      <div class="card"><span class="ph ph--grey" role="img" aria-label="Grey vinyl plank product"></span><div class="card__body">Grey waterproof vinyl plank<div class="card__price">$2.79 / sq ft</div></div><span class="card__btn">Add to Cart</span></div>
    </div>
  </div>
  <div class="banner ph ph--room" role="img" aria-label="Family relaxing together on a new wood floor">
    <div class="banner__text"><h3>BUY MORE<br>SAVE MORE</h3><p>Save up to 20% on bulk orders</p><span>Shop Now</span></div>
  </div>
  <div class="section best">
    <h2 class="section__title">Best sellers</h2>
    <div class="grid4">
      <div class="card"><span class="ph ph--dark" role="img" aria-label="Dark hardwood best seller"></span><div class="card__body">Rustic hickory hardwood plank<div class="card__price">$3.99 / sq ft</div></div></div>
      <div class="card"><span class="ph ph--wood" role="img" aria-label="Honey laminate best seller"></span><div class="card__body">Honey maple laminate plank<div class="card__price">$1.89 / sq ft</div></div></div>
      <div class="card"><span class="ph ph--grey" role="img" aria-label="Grey tile best seller"></span><div class="card__body">Slate look porcelain tile<div class="card__price">$2.49 / sq ft</div></div></div>
      <div class="card"><span class="ph ph--stone" role="img" aria-label="Beige carpet best seller"></span><div class="card__body">Soft beige plush carpet<div class="card__price">$1.59 / sq ft</div></div></div>
    </div>
  </div>
  <div class="reviews">
    <h2 class="section__title">Customer Reviews</h2>
    <div class="grid3">
      <div class="review"><div class="review__stars">★★★★★</div>Great selection and fast delivery. Our new floors look beautiful and the install went smoothly.<b>Sarah M.</b></div>
      <div class="review"><div class="review__stars">★★★★★</div>Helpful staff answered every question. The samples made choosing the right color easy.<b>David R.</b></div>
      <div class="review"><div class="review__stars">★★★★★</div>Fair prices for contractors and quick shipping to the job site. Will order again.<b>Linda K.</b></div>
    </div>
  </div>
  <div class="section recommended">
    <h2 class="section__title">Recommended For You</h2>
    <div class="grid4">
      <span class="ph ph--wood" role="img" aria-label="Light wood floor in a living room"></span>
      <span class="ph ph--dark" role="img" aria-label="Kitchen with red tile floor"></span>
      <span class="ph ph--stone" role="img" aria-label="Bright hallway with stone tile"></span>
      <span class="ph ph--wood" role="img" aria-label="Sunlit wood deck boards"></span>
    </div>
  </div>
  <div class="section history">
    <h2 class="section__title">Our History</h2>
    <div class="history__row">
      <span class="ph ph--dark" role="img" aria-label="Warm room with dark wood floor and red chair"></span>
      <div class="history__text">
        <p>We started as a small family store with one goal: help every home find a floor it loves, at a price that feels fair.</p>
        <p>Today we serve homeowners, builders, designers and hotels across the country with hardwood, laminate, tile, stone and carpet.</p>
        <p>Our team still treats every order like it is going into our own home.</p>
        <span class="btn">Read More</span>
      </div>
    </div>
  </div>
  <div class="section blogs">
    <h2 class="section__title">Latest Blogs</h2>
    <div class="grid3">
      <div class="blog"><span class="ph ph--grey" role="img" aria-label="Modern room with grey floor"></span><h5>Choosing the right plank</h5><p>Tips to match width and tone to your room.</p></div>
      <div class="blog"><span class="ph ph--wood" role="img" aria-label="Open room with wood floor"></span><h5>Caring for hardwood</h5><p>Simple habits that keep floors looking new.</p></div>
      <div class="blog"><span class="ph ph--room" role="img" aria-label="Bright living room interior"></span><h5>Tile trends this year</h5><p>Large formats and soft natural colors.</p></div>
    </div>
  </div>
  <div class="signup">
    <h3>Sign Up Special Promotions</h3>
    <form><span class="signup__input">Enter your email</span><span class="signup__btn">Subscribe</span></form>
  </div>
  <div class="payments"><div class="payments__cards"><i></i><i></i><i></i><i></i></div><span class="payments__note">Secure Checkout</span></div>
  <footer class="footer">
    <div><h6>Contact</h6><ul><li>1-800-555-0142</li><li>hello@plankhaven.example</li><li>Mon–Sat 8am–6pm</li></ul></div>
    <div><h6>My Account</h6><ul><li>Sign In</li><li>Order History</li><li>Wish List</li><li>Track Order</li></ul></div>
    <div><h6>Information</h6><ul><li>About Us</li><li>Shipping</li><li>Returns</li><li>Financing</li></ul></div>
    <div><h6>Our Support</h6><ul><li>Help Center</li><li>Install Guides</li><li>Trade Program</li></ul><div class="socials"><i></i><i></i><i></i><i></i></div></div>
  </footer>
  <div class="footbar"><span>© Plankhaven. All rights reserved.</span><span>Privacy · Terms</span></div>
</section>

<!-- Variant B: light review band -->
<section class="page page--b">
  <div class="topbar"></div>
  <header class="header">
    <div class="brand"><span class="brand__mark"></span>Plankhaven</div>
    <div class="search">Search products… <span class="search__btn"></span></div>
    <div class="contact"><div><b>1-800-555-0142</b>Call us today</div><div><b>hello@plankhaven.example</b>Email support</div></div>
  </header>
  <nav class="nav"><a class="is-active">Home</a><a>Hardwood</a><a>Laminate</a><a>Waterproof</a><a>Tile &amp; Stone</a><a>Carpet</a><a>Accessories</a><a>Blog</a></nav>
  <div class="hero ph ph--room" role="img" aria-label="Bright living room with light wood plank flooring">
    <span class="hero__title">UPGRADE YOUR FLOORS</span>
    <div class="hero__dots"><i></i><i></i><i></i></div>
  </div>
  <div class="promo">
    <div class="promo__cell"><span class="promo__big">3%</span><span class="promo__small">Off your<br>first order</span></div>
    <div class="promo__cell"><span class="promo__big">12</span><span class="promo__small">Months<br>financing</span></div>
    <div class="promo__cell"><span class="promo__big">$99</span><span class="promo__small">Flat rate<br>shipping</span></div>
  </div>
  <div class="features">
    <div class="feature"><svg viewBox="0 0 26 26"><rect x="3" y="8" width="20" height="14" fill="none" stroke="#ee7d1c" stroke-width="2"/><path d="M3 8l10-5 10 5" fill="none" stroke="#ee7d1c" stroke-width="2"/></svg><h4>FREE SAMPLES</h4><p>Try before you buy</p></div>
    <div class="feature"><svg viewBox="0 0 26 26"><rect x="2" y="9" width="14" height="10" fill="none" stroke="#ee7d1c" stroke-width="2"/><path d="M16 12h5l3 4v3h-8" fill="none" stroke="#ee7d1c" stroke-width="2"/><circle cx="7" cy="21" r="2" fill="#ee7d1c"/><circle cx="20" cy="21" r="2" fill="#ee7d1c"/></svg><h4>FAST DELIVERY</h4><p>Nationwide shipping</p></div>
    <div class="feature"><svg viewBox="0 0 26 26"><path d="M13 3l9 4v6c0 6-4 9-9 10-5-1-9-4-9-10V7z" fill="none" stroke="#ee7d1c" stroke-width="2"/><path d="M9 13l3 3 5-6" fill="none" stroke="#ee7d1c" stroke-width="2"/></svg><h4>PRICE MATCH</h4><p>Best price promise</p></div>
    <div class="feature"><svg viewBox="0 0 26 26"><path d="M5 5h4l3 6-2 2a12 12 0 005 5l2-2 6 3v4c-10 1-19-8-18-18z" fill="none" stroke="#ee7d1c" stroke-width="2"/></svg><h4>EXPERT HELP</h4><p>Talk to a specialist</p></div>
  </div>
  <div class="section cats">
    <h2 class="section__title">Shop Popular Categories</h2>
    <div class="grid4">
      <div class="cat"><span class="ph ph--dark" role="img" aria-label="Hardwood flooring sample"></span><p>Hardwood Flooring</p></div>
      <div class="cat"><span class="ph ph--wood" role="img" aria-label="Laminate flooring sample"></span><p>Laminate Flooring</p></div>
      <div class="cat"><span class="ph ph--stone" role="img" aria-label="Porcelain tile sample"></span><p>Porcelain Tile</p></div>
      <div class="cat"><span class="ph ph--grey" role="img" aria-label="Waterproof vinyl flooring sample"></span><p>Waterproof Flooring</p></div>
    </div>
  </div>
  <div class="section products">
    <h2 class="section__title">Featured Products</h2>
    <div class="grid4">
      <div class="card"><span class="ph ph--wood" role="img" aria-label="Oak plank product"></span><div class="card__body">Natural oak plank, 5 in wide<div class="card__price">$3.49 / sq ft</div></div><span class="card__btn">Add to Cart</span></div>
      <div class="card"><span class="ph ph--dark" role="img" aria-label="Walnut plank product"></span><div class="card__body">Walnut hand-scraped plank<div class="card__price">$4.29 / sq ft</div></div><span class="card__btn">Add to Cart</span></div>
      <div class="card"><span class="ph ph--stone" role="img" aria-label="Marble tile product"></span><div class="card__body">Honed marble tile, 12 x 24<div class="card__price">$5.99 / sq ft</div></div><span class="card__btn">Add to Cart</span></div>
      <div class="card"><span class="ph ph--grey" role="img" aria-label="Grey vinyl plank product"></span><div class="card__body">Grey waterproof vinyl plank<div class="card__price">$2.79 / sq ft</div></div><span class="card__btn">Add to Cart</span></div>
    </div>
  </div>
  <div class="banner ph ph--room" role="img" aria-label="Family relaxing together on a new wood floor">
    <div class="banner__text"><h3>BUY MORE<br>SAVE MORE</h3><p>Save up to 20% on bulk orders</p><span>Shop Now</span></div>
  </div>
  <div class="section best">
    <h2 class="section__title">Best sellers</h2>
    <div class="grid4">
      <div class="card"><span class="ph ph--dark" role="img" aria-label="Dark hardwood best seller"></span><div class="card__body">Rustic hickory hardwood plank<div class="card__price">$3.99 / sq ft</div></div></div>
      <div class="card"><span class="ph ph--wood" role="img" aria-label="Honey laminate best seller"></span><div class="card__body">Honey maple laminate plank<div class="card__price">$1.89 / sq ft</div></div></div>
      <div class="card"><span class="ph ph--grey" role="img" aria-label="Grey tile best seller"></span><div class="card__body">Slate look porcelain tile<div class="card__price">$2.49 / sq ft</div></div></div>
      <div class="card"><span class="ph ph--stone" role="img" aria-label="Beige carpet best seller"></span><div class="card__body">Soft beige plush carpet<div class="card__price">$1.59 / sq ft</div></div></div>
    </div>
  </div>
  <div class="reviews">
    <h2 class="section__title">Customer Reviews</h2>
    <div class="grid3">
      <div class="review"><div class="review__stars">★★★★★</div>Great selection and fast delivery. Our new floors look beautiful and the install went smoothly.<b>Sarah M.</b></div>
      <div class="review"><div class="review__stars">★★★★★</div>Helpful staff answered every question. The samples made choosing the right color easy.<b>David R.</b></div>
      <div class="review"><div class="review__stars">★★★★★</div>Fair prices for contractors and quick shipping to the job site. Will order again.<b>Linda K.</b></div>
    </div>
  </div>
  <div class="section recommended">
    <h2 class="section__title">Recommended For You</h2>
    <div class="grid4">
      <span class="ph ph--wood" role="img" aria-label="Light wood floor in a living room"></span>
      <span class="ph ph--dark" role="img" aria-label="Kitchen with red tile floor"></span>
      <span class="ph ph--stone" role="img" aria-label="Bright hallway with stone tile"></span>
      <span class="ph ph--wood" role="img" aria-label="Sunlit wood deck boards"></span>
    </div>
  </div>
  <div class="section history">
    <h2 class="section__title">Our History</h2>
    <div class="history__row">
      <span class="ph ph--dark" role="img" aria-label="Warm room with dark wood floor and red chair"></span>
      <div class="history__text">
        <p>We started as a small family store with one goal: help every home find a floor it loves, at a price that feels fair.</p>
        <p>Today we serve homeowners, builders, designers and hotels across the country with hardwood, laminate, tile, stone and carpet.</p>
        <p>Our team still treats every order like it is going into our own home.</p>
        <span class="btn">Read More</span>
      </div>
    </div>
  </div>
  <div class="section blogs">
    <h2 class="section__title">Latest Blogs</h2>
    <div class="grid3">
      <div class="blog"><span class="ph ph--grey" role="img" aria-label="Modern room with grey floor"></span><h5>Choosing the right plank</h5><p>Tips to match width and tone to your room.</p></div>
      <div class="blog"><span class="ph ph--wood" role="img" aria-label="Open room with wood floor"></span><h5>Caring for hardwood</h5><p>Simple habits that keep floors looking new.</p></div>
      <div class="blog"><span class="ph ph--room" role="img" aria-label="Bright living room interior"></span><h5>Tile trends this year</h5><p>Large formats and soft natural colors.</p></div>
    </div>
  </div>
  <div class="signup">
    <h3>Sign Up Special Promotions</h3>
    <form><span class="signup__input">Enter your email</span><span class="signup__btn">Subscribe</span></form>
  </div>
  <div class="payments"><div class="payments__cards"><i></i><i></i><i></i><i></i></div><span class="payments__note">Secure Checkout</span></div>
  <footer class="footer">
    <div><h6>Contact</h6><ul><li>1-800-555-0142</li><li>hello@plankhaven.example</li><li>Mon–Sat 8am–6pm</li></ul></div>
    <div><h6>My Account</h6><ul><li>Sign In</li><li>Order History</li><li>Wish List</li><li>Track Order</li></ul></div>
    <div><h6>Information</h6><ul><li>About Us</li><li>Shipping</li><li>Returns</li><li>Financing</li></ul></div>
    <div><h6>Our Support</h6><ul><li>Help Center</li><li>Install Guides</li><li>Trade Program</li></ul><div class="socials"><i></i><i></i><i></i><i></i></div></div>
  </footer>
  <div class="footbar"><span>© Plankhaven. All rights reserved.</span><span>Privacy · Terms</span></div>
</section>

</body>
</html>
```